Pregnancy and Fertility Information Website

Hello Designers,
I need a website which provide tips and information about healthy and happy pregnancy. My website name is KRE medical.

The website should provide all the information needed throughout pregnancy and beyond ranging from pregnancy tracking tools and articles about common pregnancy concerns and what to expect during pregnancy,etc.
The details about first trimester, second trimester and third trimester should be highlighted in the website.

Top Navigation
Home, Fertility, Pregnancy basics, Articles, Tips and News

I'm looking for a simple and clean design which involves captivating images and colors but it shouldn't be crowded. The design must be professional and modern. An easy to navigate layout is a must.

Green, violet, blue and light yellow colors are my favorites but i'm open to other options.

Any questions. Kindly ask

Industry/Entity Type

Medical

```html
<!DOCTYPE html>
<html lang="en">
<head>
<meta charset="utf-8">
<title>KRE medical – Healthy and Happy Pregnancy</title>
<link rel="stylesheet" href="https://fonts.googleapis.com/css2?family=Open+Sans:wght@400;600&family=Raleway:wght@300;400;500&display=swap">
<style>
:root{
  --green:#6cbf5f;
  --green-light:#8fd083;
  --blue:#1d6fb5;
  --blue-dark:#1f4fa0;
  --blue-mid:#3d95c8;
  --blue-button:#3c8fd0;
  --text-dark:#111;
  --text-grey:#9a9a9a;
  --text-body:#666;
  --footer:#232323;
  --white:#fff;
}
*{margin:0;padding:0;box-sizing:border-box}
html,body{width:1200px;height:2597px;overflow:hidden;background:var(--white)}
body{position:relative;font-family:Arial,Helvetica,sans-serif;color:var(--text-dark)}
.abs{position:absolute}

/* Header */
.brand{left:52px;top:28px;display:flex;align-items:center;gap:14px;font-family:"Raleway",sans-serif;font-size:42px;font-weight:500;color:var(--blue)}
.brand-dot{width:34px;height:34px;border-radius:50%;background:var(--green)}
.phone{right:322px;top:51px;display:flex;align-items:center;gap:8px;font-family:"Open Sans",sans-serif;font-size:20px;line-height:24px;color:#333;white-space:nowrap}
.search{left:892px;top:48px;width:214px;height:33px;border:2px solid #444;background:#fff}
.search svg{position:absolute;right:14px;top:5px}

/* Navigation */
.nav{left:0;top:111px;width:1200px;height:54px;background:var(--green)}
.nav a{position:absolute;top:0;height:54px;line-height:54px;font-family:"Open Sans",sans-serif;font-size:14px;color:var(--white);text-decoration:none;text-transform:uppercase}
.nav a.active{background:var(--green-light);padding:0 24px}
.social{position:absolute;right:92px;top:11px;display:flex;gap:6px}
.social span{width:31px;height:31px;border-radius:50%;background:rgba(255,255,255,.55)}

/* Hero */
.hero{left:0;top:165px;width:1200px;height:481px;background:linear-gradient(90deg,#e8e4de 0%,#f2f0ed 45%,#f7f7f6 100%)}
.hero-photo{left:0;top:0;width:620px;height:481px;background:radial-gradient(ellipse at 45% 45%,#e9d6c4 0%,#dcd3c8 40%,#e6e2dc 75%,transparent 100%)}
.hero-kicker{left:577px;top:121px;font-family:"Open Sans",sans-serif;font-size:21px;font-weight:400;color:#111}
.hero-title{left:573px;top:150px;font-family:"Open Sans",sans-serif;font-size:41px;font-weight:400;color:#000;letter-spacing:-.5px}
.hero-highlight{left:570px;top:213px;width:486px;height:55px;background:#fff;padding-left:12px;font-family:"Open Sans",sans-serif;font-size:50px;line-height:55px;color:var(--blue-dark)}
.hero-highlight em{font-style:normal;color:var(--green)}
.hero-text{left:585px;top:282px;width:420px;font-size:13px;line-height:19px;color:#555}

/* Welcome */
.welcome{left:0;top:646px;width:1200px;height:362px;background:var(--blue)}
.welcome h2{position:absolute;left:95px;top:58px;font-family:"Raleway",sans-serif;font-weight:400;font-size:29px;color:var(--white)}
.welcome p{position:absolute;left:95px;top:108px;width:720px;font-size:13.3px;line-height:20px;color:var(--white)}
.btn{position:absolute;left:92px;top:254px;width:235px;height:47px;line-height:47px;text-align:center;background:var(--blue-button);color:var(--white);font-size:15px}
.welcome-photo{position:absolute;left:862px;top:38px;width:196px;height:270px;border:3px solid var(--white);background:linear-gradient(160deg,#d9dee6,#efe6da 60%,#c9b8a6)}

/* Trimesters */
.card{top:1134px;width:277px;border:2px solid #e2e2e2;background:#fff}
.card h3{position:relative;height:57px;line-height:57px;text-align:center;font-family:"Raleway",sans-serif;font-weight:400;font-size:23px;color:var(--white);margin:-2px -2px 0}
.card h3::after{content:"";position:absolute;left:50%;bottom:-14px;margin-left:-16px;border-left:16px solid transparent;border-right:16px solid transparent;border-top:14px solid currentColor}
.card .pic{margin:38px 0 0 21px;width:226px;height:190px}
.card p{margin:26px 0 0 21px;width:226px;font-size:13px;line-height:19px;color:var(--text-grey)}
.t1 h3{background:var(--blue-dark)} .t1 h3::after{border-top-color:var(--blue-dark)}
.t2 h3{background:var(--green)} .t2 h3::after{border-top-color:var(--green)}
.t3 h3{background:var(--blue-mid)} .t3 h3::after{border-top-color:var(--blue-mid)}
.t1 .pic{background:radial-gradient(circle at 45% 50%,#e4804a,#a8402a 45%,#1c2240 100%)}
.t2 .pic{background:radial-gradient(circle at 50% 50%,#e09080,#b0403a 50%,#4a1614 100%)}
.t3 .pic{background:radial-gradient(circle at 55% 45%,#f0b0a0,#b0405a 50%,#3a0e20 100%)}

/* Tips */
.tips-photo{left:0;top:1687px;width:636px;height:431px;background:linear-gradient(120deg,#d8c5b4 0%,#efe6df 45%,#e3dbd6 100%)}
.tips{left:636px;top:1687px;width:564px;height:431px;background:var(--blue)}
.tips h2{position:absolute;left:57px;top:50px;font-family:"Raleway",sans-serif;font-weight:400;font-size:24px;color:var(--white)}
.tip{position:absolute;left:53px;display:flex;align-items:center;gap:18px}
.tip b{width:55px;height:55px;border-radius:50%;display:flex;align-items:center;justify-content:center;font-family:"Raleway",sans-serif;font-weight:400;font-size:24px;color:var(--white)}
.tip span{width:330px;font-size:13px;line-height:19px;color:var(--white)}
.tip.blue b{background:var(--blue-mid)} .tip.green b{background:var(--green)}

/* Articles */
.articles-title{left:92px;top:2170px;font-family:"Raleway",sans-serif;font-weight:400;font-size:27px;color:#333}
.article{width:500px}
.article time{display:block;font-family:"Raleway",sans-serif;font-size:15px;color:#333}
.article .lead{margin-top:8px;width:470px;font-size:13.5px;line-height:19px;color:var(--text-body)}
.article .pic{position:absolute}
.article .side{position:absolute;width:245px;font-size:13px;line-height:19px;color:var(--text-body)}
.article .more{position:absolute;font-size:13px;color:var(--green)}
.article .more i{font-style:normal;color:#333}
.divider{left:606px;top:2232px;width:1px;height:215px;background:#ddd}

/* Footer */
.footer{left:0;top:2507px;width:1200px;height:90px;background:var(--footer);text-align:center;color:var(--white)}
.footer nav{padding-top:27px;font-size:15.5px}
.footer nav a{color:var(--white);text-decoration:none}
.footer small{display:block;margin-top:10px;font-size:10px}
</style>
</head>
<body>

<header>
  <div class="abs brand"><span class="brand-dot"></span>KRE medical</div>
  <div class="abs phone">
    <svg width="20" height="20" viewBox="0 0 20 20" aria-hidden="true"><rect width="20" height="20" rx="3" fill="#1f4fa0"/><path d="M6 4c1 0 2 2 2 3s-1 1-1 2 2 3 3 3 1-1 2-1 3 1 3 2-1 2-2 2C8 15 5 11 5 6c0-1 0-2 1-2z" fill="#fff"/></svg>
    +1-555-010-2040
  </div>
  <div class="abs search">
    <svg width="24" height="22" viewBox="0 0 24 22" aria-hidden="true"><circle cx="9" cy="9" r="6" fill="none" stroke="#333" stroke-width="2.5"/><path d="M13.5 13.5L21 20" stroke="#333" stroke-width="3.5" stroke-linecap="round"/></svg>
  </div>
</header>

<nav class="abs nav">
  <a class="active" style="left:92px" href="#">Home</a>
  <a style="left:190px" href="#">Fertility</a>
  <a style="left:298px" href="#">Pragnancy Basics</a>
  <a style="left:468px" href="#">Articles</a>
  <a style="left:565px" href="#">Tips and News</a>
  <div class="social"><span></span><span></span><span></span><span></span><span></span></div>
</nav>

<section class="abs hero">
  <div class="abs hero-photo" role="img" aria-label="Photo of a smiling pregnant woman sitting cross-legged on a sofa"></div>
  <p class="abs hero-kicker">WE PROVIDE INFORMATION ABOUT</p>
  <h1 class="abs hero-title">ABOUT HEALTHY AND</h1>
  <div class="abs hero-highlight"><em>HAPPY</em> PREGNANCY</div>
  <p class="abs hero-text">simply dummy text of the printing and typesetting industry. Lorem Ipsum has been the industry's standard dummy text ever since the 1500s, when an unknown printer took a galley of type and scrambled it to make a type specimen book.</p>
</section>

<section class="abs welcome">
  <h2>Welcome to KRE Medical health care</h2>
  <p>simply dummy text of the printing and typesetting industry. Lorem Ipsum has been the industry's standard dummy text ever since the 1500s, when an unknown printer took a galley of type and scrambled it to make a type specimen book. It has survived not only five centuries but also the leap into electronic typesetting, remaining essentially unchanged. It was popu-larised in the 1960s with the release of Letraset sheets containing Lorem Ipsum passages, and more recently with desktop publishing software like Aldus PageMaker including versions of Lorem Ipsum.</p>
  <a class="btn">Read more</a>
  <div class="welcome-photo" role="img" aria-label="Photo of a doctor examining a pregnant patient"></div>
</section>

<section>
  <article class="abs card t1" style="left:137px;height:451px">
    <h3>First Trimester</h3>
    <div class="pic" role="img" aria-label="Image of an early-stage embryo"></div>
    <p>simply dummy text of the printing and typesetting industry. Lorem Ipsum has been the industry's standard dummy text ever since the 1500s, when an unknown printer took a galley of type and scrambled it to make a type .</p>
  </article>
  <article class="abs card t2" style="left:464px;height:459px">
    <h3>Second Trimester</h3>
    <div class="pic" role="img" aria-label="Image of a developing fetus in the second trimester"></div>
    <p>simply dummy text of the printing and typesetting industry. Lorem Ipsum has been the industry's standard dummy text ever since the 1500s, when an unknown printer took a galley of type and scrambled it to make a type .</p>
  </article>
  <article class="abs card t3" style="left:783px;height:459px">
    <h3>Third Trimester</h3>
    <div class="pic" role="img" aria-label="Image of a fetus in the third trimester"></div>
    <p>simply dummy text of the printing and typesetting industry. Lorem Ipsum has been the industry's standard dummy text ever since the 1500s, when an unknown printer took a galley of type and scrambled it to make a type speci</p>
  </article>
</section>

<div class="abs tips-photo" role="img" aria-label="Photo of a smiling woman looking at a pregnancy test"></div>
<section class="abs tips">
  <h2>Tips and News</h2>
  <div class="tip blue" style="top:108px"><b>1.</b><span>Simply dummy text of the printing and typesetting industry. Lorem Ipsum has been t..</span></div>
  <div class="tip green" style="top:179px"><b>2.</b><span>Simply dummy text of the printing and typesetting industry. Lorem Ipsum has been t..</span></div>
  <div class="tip blue" style="top:253px"><b>3.</b><span>Simply dummy text of the printing and typesetting industry. Lorem Ipsum has been t..</span></div>
  <div class="tip green" style="top:329px"><b>4.</b><span>Simply dummy text of the printing and typesetting industry. Lorem Ipsum has been t..</span></div>
</section>

<section>
  <h2 class="abs articles-title">Latest Articles</h2>
  <article class="abs article" style="left:92px;top:2219px">
    <time>10 February 2017</time>
    <p class="lead">Simply dummy text of the printing and typesetting industry. Lorem Ipsum has been t..</p>
    <div class="pic" role="img" aria-label="Photo of a happy couple holding a pregnancy test" style="left:0;top:91px;width:225px;height:135px;background:linear-gradient(135deg,#e9ddd0,#d7b8a0 50%,#f3ede6)"></div>
    <p class="side" style="left:247px;top:101px">Simply dummy text of the printing and typesetting industry. Lorem Ipsum has been the industry's standard dummy text ever since the</p>
    <span class="more" style="left:247px;top:185px">Read more <i>&gt;&gt;</i></span>
  </article>
  <div class="abs divider"></div>
  <article class="abs article" style="left:641px;top:2226px">
    <time>11 February 2017</time>
    <p class="lead">Simply dummy text of the printing and typesetting industry. Lorem Ipsum has been t..</p>
    <div class="pic" role="img" aria-label="Photo of a pregnant woman having an ultrasound scan" style="left:5px;top:79px;width:201px;height:133px;background:linear-gradient(135deg,#dfe6ee,#c9d3de 50%,#eef0f3)"></div>
    <p class="side" style="left:233px;top:88px">Simply dummy text of the printing and typesetting industry. Lorem Ipsum has been the industry's standard dummy text ever since</p>
    <span class="more" style="left:233px;top:181px">Read more <i>&gt;&gt;</i></span>
  </article>
</section>

<footer class="abs footer">
  <nav><a href="#">Home</a> &nbsp;|&nbsp; <a href="#">Fertility</a> &nbsp;|&nbsp; <a href="#">Pragnancy Basics</a> &nbsp;|&nbsp; <a href="#">Articles</a> &nbsp;|&nbsp; <a href="#">Tips and News</a> &nbsp;|&nbsp; <a href="#">Contact Us</a> &nbsp;|&nbsp; <a href="#">Testimonials</a></nav>
  <small>Copyright 2017 | KRE medical</small>
</footer>

</body>
</html>
```